Brightmoor Dental Care Stationery

create stationery, business cards and envelops for business. Use current logo on website but open to new fonts for the business name. Business name is Brightmoor Dental Care, would like below the name added "Cosmetic - Family - Implants" Website is www.brightmoordentalcareXQ.example. I would like to have modern look, clean, and professional. The water mark of the logo is a great thing to ad as well.

Target Market(s)

General public, Families, Cosmetic, Implant

Industry/Entity Type

Dental

Font styles to use
Sans Serif

Colors
9bcb3c
000000
757575
c9c9c9

Requirements
Must have
• Would like to see different versions of the current logo. Improvements, color, sytle, and class.
Nice to have
• current font has double "oo" in the Brightmoor logo, does not need to have with new logo.

```html
<!DOCTYPE html>
<html lang="en">
<head>
<meta charset="utf-8">
<title>Brightmoor Dental Care Stationery</title>
<link href="https://fonts.googleapis.com/css2?family=Lato:wght@400;700;900&display=swap" rel="stylesheet">
<style>
:root{
  --blue:#0f7cc3;
  --green:#8dc63f;
  --ink:#222;
  --grey:#757575;
  --mark:#c9c9c9;
  --paper:#ffffff;
  --ground:#eeeeee;
}
*{margin:0;padding:0;box-sizing:border-box}
html,body{width:1200px;height:795px;overflow:hidden}
body{background:var(--ground);font-family:"Lato",sans-serif;position:relative;color:var(--ink)}
.piece{position:absolute;background:var(--paper);overflow:hidden;box-shadow:0 2px 6px rgba(0,0,0,.12)}
.piece svg.art{position:absolute;left:0;top:0}
.brand{position:absolute;display:flex;align-items:center}
.brand-dot{border:3px solid var(--green);border-radius:50%;flex:none}
.brand-name{font-weight:900;color:var(--blue);text-transform:uppercase;line-height:1.05;white-space:nowrap}
.contact{position:absolute;font-size:6.2px;line-height:1.4;color:var(--ink);white-space:nowrap}
.contact li{list-style:none;display:flex;gap:4px;align-items:flex-start}
.contact .ico{width:5px;height:5px;border-radius:50%;background:var(--green);margin-top:2px;flex:none}
.divider{position:absolute;width:1px;background:var(--mark)}

/* letterhead */
.letterhead{left:290px;top:94px;width:311px;height:438px}
/* folder */
.folder{left:632px;top:66px;width:349px;height:463px}
.folder .url{position:absolute;left:0;right:0;bottom:12px;text-align:center;color:#fff;font-size:7px}
/* business cards */
.card-front{left:178px;top:549px;width:147px;height:84px}
.card-back{left:178px;top:642px;width:147px;height:84px;background:var(--blue)}
.card-back .tagline{position:absolute;left:0;right:0;top:61px;text-align:center;color:#fff;font-size:4.5px}
.card-back .url{position:absolute;left:0;right:0;top:68px;text-align:center;color:var(--green);font-size:4.5px}
.holder{position:absolute;left:10px;top:32px;font-size:6px;font-weight:700;color:var(--blue)}
/* envelopes */
.envelope-front{left:332px;top:561px;width:366px;height:159px}
.envelope-back{left:712px;top:559px;width:369px;height:161px}
</style>
</head>
<body>

<!-- Letterhead -->
<section class="piece letterhead">
  <svg class="art" width="311" height="438" viewBox="0 0 311 438" aria-hidden="true">
    <circle cx="200" cy="285" r="95" fill="none" stroke="var(--mark)" stroke-width="7" opacity=".7"/>
    <path d="M0,374 Q155,424 311,366 L311,376 Q155,432 0,384 Z" fill="var(--green)"/>
    <path d="M0,388 Q155,436 311,380 V438 H0 Z" fill="var(--blue)"/>
  </svg>
  <div class="brand" style="left:22px;top:24px;gap:6px">
    <span class="brand-dot" style="width:30px;height:30px"></span>
    <span class="brand-name" style="font-size:11px">Brightmoor<br>Dental Care</span>
  </div>
  <span class="divider" style="left:164px;top:22px;height:46px"></span>
  <ul class="contact" style="left:174px;top:22px">
    <li><span class="ico"></span><span>1820 N Alder Ave<br>Millbrook, XQ 00000-0000</span></li>
    <li><span class="ico"></span><span>555-014-2870</span></li>
    <li><span class="ico"></span><span>hello@brightmoor.example</span></li>
    <li><span class="ico"></span><span>www.brightmoordentalcareXQ.example</span></li>
  </ul>
</section>

<!-- Presentation folder -->
<section class="piece folder">
  <svg class="art" width="349" height="463" viewBox="0 0 349 463" aria-hidden="true">
    <path d="M0,126 Q175,246 349,122 L349,132 Q175,254 0,136 Z" fill="var(--green)"/>
    <path d="M0,140 Q175,262 349,136 V463 H0 Z" fill="var(--blue)"/>
    <circle cx="243" cy="352" r="92" fill="none" stroke="#0b5f98" stroke-width="6" opacity=".55"/>
  </svg>
  <div class="brand" style="left:66px;top:44px;gap:10px">
    <span class="brand-dot" style="width:62px;height:62px;border-width:4px"></span>
    <span class="brand-name" style="font-size:24px">Brightmoor<br>Dental Care</span>
  </div>
  <p class="url">www.brightmoordentalcareXQ.example</p>
</section>

<!-- Business card front -->
<section class="piece card-front">
  <svg class="art" width="147" height="84" viewBox="0 0 147 84" aria-hidden="true">
    <circle cx="116" cy="34" r="25" fill="none" stroke="var(--mark)" stroke-width="2.5" opacity=".7"/>
    <path d="M0,64 Q74,76 147,62 L147,66 Q74,80 0,68 Z" fill="var(--green)"/>
    <path d="M0,70 Q74,82 147,68 V84 H0 Z" fill="var(--blue)"/>
  </svg>
  <div class="brand" style="left:10px;top:10px;gap:3px">
    <span class="brand-dot" style="width:13px;height:13px;border-width:1.5px"></span>
    <span class="brand-name" style="font-size:6px">Brightmoor<br>Dental Care</span>
  </div>
  <p class="holder">Lena M. Ortiz DDS</p>
  <ul class="contact" style="left:10px;top:41px;font-size:3.6px">
    <li><span class="ico" style="width:2.5px;height:2.5px;margin-top:1px"></span><span>555-014-2870</span></li>
    <li><span class="ico" style="width:2.5px;height:2.5px;margin-top:1px"></span><span>hello@brightmoor.example</span></li>
    <li><span class="ico" style="width:2.5px;height:2.5px;margin-top:1px"></span><span>www.brightmoordentalcareXQ.example</span></li>
    <li><span class="ico" style="width:2.5px;height:2.5px;margin-top:1px"></span><span>1820 N Alder Ave<br>Millbrook, XQ 00000-0000</span></li>
  </ul>
</section>

<!-- Business card back -->
<section class="piece card-back">
  <div class="brand" style="left:36px;top:24px;gap:4px">
    <span class="brand-dot" style="width:20px;height:20px;border-width:2px"></span>
    <span class="brand-name" style="font-size:8px;color:#fff">Brightmoor<br>Dental Care</span>
  </div>
  <p class="tagline">Cosmetic - Family - Implants</p>
  <p class="url">www.brightmoordentalcareXQ.example</p>
</section>

<!-- DL envelope front -->
<section class="piece envelope-front">
  <svg class="art" width="366" height="159" viewBox="0 0 366 159" aria-hidden="true">
    <circle cx="310" cy="54" r="52" fill="none" stroke="var(--mark)" stroke-width="5" opacity=".7"/>
    <path d="M0,114 Q190,140 366,106 L366,114 Q190,148 0,122 Z" fill="var(--green)"/>
    <path d="M0,126 Q190,152 366,118 V159 H0 Z" fill="var(--blue)"/>
  </svg>
  <div class="brand" style="left:24px;top:24px;gap:5px">
    <span class="brand-dot" style="width:27px;height:27px;border-width:2.5px"></span>
    <span class="brand-name" style="font-size:10px">Brightmoor<br>Dental Care</span>
  </div>
  <span class="divider" style="left:146px;top:28px;height:34px"></span>
  <p class="contact" style="left:154px;top:30px;font-size:6.5px">1820 N Alder Ave,<br>Millbrook,<br>XQ 00000-0000</p>
</section>

<!-- DL envelope back -->
<section class="piece envelope-back">
  <svg class="art" width="369" height="161" viewBox="0 0 369 161" aria-hidden="true">
    <path d="M0,0 H369 L353,38 Q349,46 340,46 H29 Q20,46 16,38 Z" fill="var(--green)"/>
    <circle cx="185" cy="22" r="13" fill="none" stroke="#fff" stroke-width="2"/>
  </svg>
</section>

</body>
</html>
```